Business Card for a Dental Office

The design should communicate integrity, quality and reliability. We also want the card look elegant, simple, but still stand out, different from the traditional-dental-office business card.

Business

```html
<!DOCTYPE html>
<html lang="en">
<head>
<meta charset="utf-8">
<title>Halden Dental Studio – Business &amp; Appointment Cards</title>
<link href="https://fonts.googleapis.com/css2?family=Oswald:wght@500&family=Montserrat:wght@400;600&family=Roboto+Condensed:wght@400&display=swap" rel="stylesheet">
<style>
  :root {
    --backdrop: #ece8e2;
    --card: #ffffff;
    --ink: #111111;
    --gold: #c9a81c;
    --gold-light: #e2c93a;
    --rule: #222222;
    --white: #ffffff;
  }
  * { box-sizing: border-box; margin: 0; padding: 0; }
  html, body { width: 1200px; height: 800px; overflow: hidden; }
  body {
    background: var(--backdrop);
    position: relative;
    font-family: "Montserrat", sans-serif;
    color: var(--ink);
  }
  .card {
    position: absolute;
    left: 290px;
    width: 620px;
    height: 354px;
    background: var(--card);
    border-radius: 14px;
    overflow: hidden;
    box-shadow: 0 6px 18px rgba(0,0,0,0.18);
  }
  .business-card { top: 32px; }
  .appointment-card { top: 414px; }

  .card-band { position: absolute; inset: 0; }

  .brand {
    position: absolute;
    display: flex;
    align-items: center;
    gap: 12px;
  }
  .brand-mark {
    flex: none;
    background: var(--gold);
  }
  .brand-name {
    font-family: "Oswald", sans-serif;
    font-weight: 500;
    color: var(--ink);
    letter-spacing: 0.5px;
    line-height: 1;
  }

  /* Business card */
  .business-card .brand { left: 0; right: 0; top: 84px; justify-content: center; }
  .business-card .brand-mark { width: 42px; height: 42px; }
  .business-card .brand-name { font-size: 32px; }

  .holder {
    position: absolute;
    left: 0; right: 0;
    top: 228px;
    text-align: center;
  }
  .holder-name {
    font-weight: 600;
    font-size: 19px;
    color: var(--gold-light);
    letter-spacing: 1px;
  }
  .holder-title {
    font-size: 13px;
    color: var(--white);
    margin-top: 4px;
  }
  .contact {
    position: absolute;
    right: 42px;
    top: 290px;
    text-align: right;
    color: var(--white);
    font-size: 12.5px;
    font-style: normal;
    line-height: 1.65;
  }

  /* Appointment card */
  .appointment-card .brand { left: 40px; top: 44px; }
  .appointment-card .brand-mark { width: 30px; height: 30px; }
  .appointment-card .brand-name { font-size: 22px; }
  .appointment-title {
    position: absolute;
    right: 44px; top: 92px;
    font-family: "Oswald", sans-serif;
    font-weight: 500;
    font-size: 22px;
    color: var(--gold);
    letter-spacing: 0.5px;
  }
  .form-field {
    position: absolute;
    display: flex;
    align-items: flex-end;
    font-family: "Roboto Condensed", sans-serif;
    font-size: 15px;
    text-transform: uppercase;
  }
  .form-field .field-line {
    border-bottom: 1px solid var(--rule);
    margin-left: 8px;
    height: 14px;
  }
  .field-name { left: 44px; top: 142px; }
  .field-name .field-line { width: 470px; }
  .field-date { left: 44px; top: 190px; }
  .field-date .field-line { width: 190px; }
  .field-time { left: 330px; top: 190px; }
  .field-time .field-line { width: 122px; }
  .field-time .meridiem { margin-left: 12px; letter-spacing: 1px; }

  .weekdays {
    position: absolute;
    left: 44px; right: 44px; top: 238px;
    display: flex;
    justify-content: space-between;
    list-style: none;
    font-family: "Roboto Condensed", sans-serif;
    font-size: 14px;
    text-transform: uppercase;
  }
  .weekdays li { display: flex; align-items: center; gap: 8px; }
  .checkbox {
    width: 17px; height: 17px;
    border: 2px solid var(--ink);
    border-radius: 2px;
  }
  .notice {
    position: absolute;
    left: 44px; right: 44px; top: 290px;
    font-family: "Roboto Condensed", sans-serif;
    font-size: 15px;
    text-align: center;
  }
</style>
</head>
<body>

<section class="card business-card" aria-label="Business card">
  <svg class="card-band" width="620" height="354" viewBox="0 0 620 354" aria-hidden="true">
    <defs>
      <linearGradient id="goldSweep" x1="0" x2="1" y1="0" y2="0">
        <stop offset="0" stop-color="#a88a12"/>
        <stop offset="0.5" stop-color="#e2c93a"/>
        <stop offset="1" stop-color="#b8981a"/>
      </linearGradient>
    </defs>
    <path d="M0,212 Q300,176 620,166 L620,184 Q310,190 0,222 Z" fill="url(#goldSweep)"/>
    <path d="M0,222 Q310,190 620,184 L620,354 L0,354 Z" fill="#111111"/>
  </svg>

  <div class="brand">
    <span class="brand-mark" aria-hidden="true"></span>
    <div class="brand-name">HALDEN DENTAL STUDIO</div>
  </div>

  <div class="holder">
    <div class="holder-name">JORDAN PIERCE</div>
    <div class="holder-title">General Manager</div>
  </div>

  <address class="contact">
    127 Willow Lane, Fairview, GA 30412<br>
    Tel: (555) 014-2398 · Email hello@haldendental.com · www.haldendental.com
  </address>
</section>

<section class="card appointment-card" aria-label="Appointment card">
  <div class="brand">
    <span class="brand-mark" aria-hidden="true"></span>
    <div class="brand-name">HALDEN DENTAL STUDIO</div>
  </div>

  <h2 class="appointment-title">APPOINTMENT CARD</h2>

  <div class="form-field field-name">Name<span class="field-line"></span></div>
  <div class="form-field field-date">Date<span class="field-line"></span></div>
  <div class="form-field field-time">Time<span class="field-line"></span><span class="meridiem">AM&nbsp; PM</span></div>

  <ul class="weekdays">
    <li><span class="checkbox"></span>Mon.</li>
    <li><span class="checkbox"></span>Tues.</li>
    <li><span class="checkbox"></span>Wed.</li>
    <li><span class="checkbox"></span>Thur.</li>
    <li><span class="checkbox"></span>Fri.</li>
    <li><span class="checkbox"></span>Sat.</li>
  </ul>

  <p class="notice">If you are unable to keep your appointment, please call us within 24 hours.</p>
</section>

</body>
</html>
```